Environmental Engineering Site Design

http://kvolmerassoc.com/ is the current website that we currently have however we are looking for a new design. We are really looking for something very close to Brindle's website. Expanding on that, we want our website to be very much like a software development company. Icon, and imagery driven with short descriptions is a plus unlike our current site. We want the site to be very clean, good subtle but power typography, and very modern. Colors we are looking to stay around a mainly blues and grays though we do value color input but please keep it toned down. Other sites that we like are:
http://www.brindle-example.com/
http://www.qt-z.com/
http://www.norvalyx.com/
http://ofu.com/
Industry/Entity Type
Software
Requirements
Must have
- Client login button/section somewhere, blog posts, and news.

```html
<!DOCTYPE html>
<html lang="en">
<head>
<meta charset="utf-8">
<title>Kvolmer Partners — Environmental Consulting &amp; Site Restoration</title>
<link href="https://fonts.googleapis.com/css2?family=Oswald:wght@500&family=PT+Sans:ital,wght@0,400;0,700;1,400;1,700&family=PT+Sans+Narrow:wght@400;700&display=swap" rel="stylesheet">
<style>
:root{
  --brand-blue:#2d5fa6;
  --heading-navy:#25487a;
  --nav-top:#5b7fb4;
  --nav-bottom:#22467f;
  --nav-divider:#6e8fbf;
  --accent-green:#7bb32e;
  --text-dark:#1a1a1a;
  --rule-gray:#d6d6d6;
  --page-bg:#ffffff;
}
*{margin:0;padding:0;box-sizing:border-box}
html,body{width:1200px;height:1150px;overflow:hidden;background:var(--page-bg)}
body{position:relative;font-family:"PT Sans",Arial,sans-serif;color:var(--text-dark)}
.site-logo{position:absolute;left:122px;top:66px;display:flex;align-items:center;gap:10px}
.site-logo .logo-dot{width:26px;height:26px;border-radius:50%;background:var(--brand-blue)}
.site-logo .logo-name{font-weight:700;font-size:28px;color:var(--brand-blue)}
.site-tagline{position:absolute;right:112px;top:97px;font-family:"PT Sans Narrow",Arial,sans-serif;font-weight:700;font-size:27px;color:var(--brand-blue);letter-spacing:-.6px}
.main-nav{position:absolute;left:116px;top:160px;width:981px;height:42px;border-radius:3px 3px 0 0;background:linear-gradient(var(--nav-top),var(--nav-bottom));display:flex;align-items:center}
.main-nav a{color:#fff;text-decoration:none;font-size:13.5px;font-weight:700;letter-spacing:-.2px;height:42px;line-height:42px;text-align:center;border-right:1px solid var(--nav-divider)}
.main-nav a:last-of-type{border-right:none}
.client-login{position:absolute;right:7px;top:7px;width:119px;height:27px;background:linear-gradient(#2a2a2a,#050505);border-radius:3px;color:#fff;font-size:12px;font-weight:700;display:flex;align-items:center;justify-content:center;gap:6px}
.hero{position:absolute;left:116px;top:202px;width:981px;height:387px;background:linear-gradient(180deg,#8fa9c6 0%,#c6d6e4 30%,#b9c8cf 52%,#4d6a36 60%,#8a9a3e 75%,#6b8d23 88%,#486b14 100%)}
.hero-shade{position:absolute;left:116px;top:202px;width:560px;height:240px;background:linear-gradient(90deg,rgba(110,110,110,.55),rgba(110,110,110,0))}
.hero-title{position:absolute;left:153px;top:286px;font-family:"Oswald",Impact,sans-serif;font-weight:500;font-size:46px;line-height:60px;color:#fff;letter-spacing:-1.2px;text-shadow:0 2px 3px rgba(0,0,0,.3)}
.hero-lede{position:absolute;left:153px;top:348px;width:500px;font-size:20px;line-height:26px;color:#fff;letter-spacing:-.6px;text-shadow:0 1px 2px rgba(0,0,0,.4)}
.section-title{position:absolute;font-style:italic;font-weight:700;font-size:22px;letter-spacing:-.6px;color:var(--heading-navy)}
.disciplines-title{left:127px;top:603px}
.discipline{position:absolute;top:634px;width:172px}
.discipline h3{font-family:"PT Sans Narrow",Arial,sans-serif;font-weight:700;font-size:17px;letter-spacing:-.2px;color:var(--heading-navy);height:31px;display:flex;justify-content:space-between;align-items:center;padding-left:4px;padding-bottom:6px}
.discipline-photo{display:block;width:172px;height:111px;border-radius:4px}
.section-divider{position:absolute;left:116px;top:806px;width:981px;height:30px;background:radial-gradient(ellipse at 50% 0,rgba(0,0,0,.10),rgba(0,0,0,0) 70%)}
.news-title{left:128px;top:839px}
.blog-title{left:617px;top:839px;color:var(--accent-green)}
.entry-date{font-style:italic;font-size:14px;line-height:20px}
.entry-body{font-size:13px;line-height:19.5px;letter-spacing:-.3px}
.news-item{position:absolute;left:129px;width:400px}
.blog-photo{position:absolute;left:617px;top:877px;width:137px;height:124px;border-radius:3px;background:linear-gradient(135deg,#6e6a5c,#b8a86a 45%,#d8c24a 60%,#5a5448)}
.blog-entry{position:absolute;left:768px;top:874px;width:310px}
.blog-entry h4{font-weight:400;font-size:21px;line-height:21px;letter-spacing:-.5px;margin:1px 0 8px}
.blog-entry .entry-body{padding-left:4px}
.site-footer{position:absolute;left:116px;top:1057px;width:981px;height:30px;border-top:1px solid var(--rule-gray);border-bottom:1px solid var(--rule-gray);font-size:12px}
.site-footer a,.site-footer span{position:absolute;top:6px;color:var(--text-dark);text-decoration:none}
</style>
</head>
<body>
<header>
  <div class="site-logo"><span class="logo-dot"></span><span class="logo-name">Kvolmer Partners</span></div>
  <div class="site-tagline">Environmental Consulting &amp; Site Restoration</div>
  <nav class="main-nav">
    <a href="#" style="width:95px">Home</a>
    <a href="#" style="width:117px">Disciplines</a>
    <a href="#" style="width:103px">Services</a>
    <a href="#" style="width:116px">Resources</a>
    <a href="#" style="width:106px">About Ut</a>
    <a href="#" style="width:116px">Contact Us</a>
    <a href="#" style="width:168px">Request Infomation</a>
    <div class="client-login">
      <svg width="12" height="15" viewBox="0 0 12 15"><path d="M3 6V4a3 3 0 0 1 6 0v2" fill="none" stroke="#fff" stroke-width="1.6"/><rect x="1" y="6" width="10" height="8" rx="1" fill="#fff"/><rect x="3" y="8.5" width="6" height="1" fill="#111"/><rect x="3" y="11" width="6" height="1" fill="#111"/></svg>
      CLIENT LOGIN
    </div>
  </nav>
</header>

<section>
  <div class="hero" role="img" aria-label="Photo of green meadow landscape under a blue sky with clouds"></div>
  <div class="hero-shade"></div>
  <h1 class="hero-title">RESTORING LAND TO LIFE</h1>
  <p class="hero-lede">Kvolmer Partners is a full-service, environmental engineering consultancy specializing in brownfields initiatives.</p>
</section>

<section>
  <h2 class="section-title disciplines-title">Our Disciplines</h2>
  <div class="discipline" style="left:125px"><h3>Environmental Science <svg width="16" height="14" viewBox="0 0 16 14"><path d="M1 1l6 6-6 6M8 1l6 6-6 6" fill="none" stroke="#7bb32e" stroke-width="2.6"/></svg></h3><div class="discipline-photo" role="img" aria-label="Photo of a river channel with green banks" style="background:linear-gradient(#5f7a3a,#8c8a78 45%,#5d6b3c)"></div></div>
  <div class="discipline" style="left:323px"><h3>Engineering <svg width="16" height="14" viewBox="0 0 16 14"><path d="M1 1l6 6-6 6M8 1l6 6-6 6" fill="none" stroke="#7bb32e" stroke-width="2.6"/></svg></h3><div class="discipline-photo" role="img" aria-label="Black and white photo of a turbine engine" style="background:radial-gradient(circle at 50% 50%,#3a3a3a,#8a8a8a 45%,#2e2e2e)"></div></div>
  <div class="discipline" style="left:522px"><h3>Biology <svg width="16" height="14" viewBox="0 0 16 14"><path d="M1 1l6 6-6 6M8 1l6 6-6 6" fill="none" stroke="#7bb32e" stroke-width="2.6"/></svg></h3><div class="discipline-photo" role="img" aria-label="Photo of a gecko silhouette on textured glass" style="background:linear-gradient(135deg,#c9c7b0,#3b3a30 55%,#bdbca4)"></div></div>
  <div class="discipline" style="left:720px"><h3>Geology <svg width="16" height="14" viewBox="0 0 16 14"><path d="M1 1l6 6-6 6M8 1l6 6-6 6" fill="none" stroke="#7bb32e" stroke-width="2.6"/></svg></h3><div class="discipline-photo" role="img" aria-label="Photo of rocky stone outcrop" style="background:linear-gradient(135deg,#5a5a58,#9c9a96 50%,#4a4844)"></div></div>
  <div class="discipline" style="left:918px"><h3>Regulatory Expertise <svg width="16" height="14" viewBox="0 0 16 14"><path d="M1 1l6 6-6 6M8 1l6 6-6 6" fill="none" stroke="#7bb32e" stroke-width="2.6"/></svg></h3><div class="discipline-photo" role="img" aria-label="Photo of an industrial power plant under blue sky" style="background:linear-gradient(#6f9ad0,#a9bfd8 45%,#8a8a86 70%,#6b6a60)"></div></div>
</section>

<div class="section-divider"></div>

<section>
  <h2 class="section-title news-title">Recent News</h2>
  <div class="news-item" style="top:875px"><p class="entry-date">November 28. 2011</p><p class="entry-body">Lorem ipsum dolor sit amet, consectetur adipisicing elit, sed do eiusmod tempor incididunt ut labore et dolore magna aliqua. Ut enim ad minim</p></div>
  <div class="news-item" style="top:944px"><p class="entry-date">November 28. 2011</p><p class="entry-body">Lorem ipsum dolor sit amet, consectetur adipisicing elit, sed do eiusmod tempor incididunt ut labore et dolore magna aliqua. Ut enim ad minim</p></div>
</section>

<section>
  <h2 class="section-title blog-title">Blog Post</h2>
  <div class="blog-photo" role="img" aria-label="Photo of an excavator demolishing an industrial building"></div>
  <article class="blog-entry">
    <p class="entry-date">November 28. 2011</p>
    <h4>Various environmentally sensitive scopes of work.</h4>
    <p class="entry-body">Lorem ipsum dolor sit amet, consectetur adipisicing elit, sed do eiusmod tempor incididunt ut labore et dolore magna aliqua. Ut enim ad minim veniam, quis nostrud</p>
  </article>
</section>

<footer class="site-footer">
  <a href="#" style="left:5px">Home</a>
  <a href="#" style="left:91px">Disciplines</a>
  <a href="#" style="left:200px">Services</a>
  <a href="#" style="left:297px">Resources</a>
  <a href="#" style="left:403px">About Ut</a>
  <a href="#" style="left:504px">Contact Us</a>
  <a href="#" style="left:610px">Request Infomation</a>
  <span style="right:0">© Kvolmer Partners 2012</span>
</footer>
</body>
</html>
```